BFO Web Site

Build a web site for Bellcrest Field Operations (BFO)

Target Market(s)

Petrochemical, Refining, and Manufacturing

Industry/Entity Type

Manufacturing

Coding

Coded - Design and coding required

Number of Pages Required

1 page

Font styles to use
Sans Serif

Colors

Designer to choose only greyscale colors for use in the design.

Requirements
Must have
• BFO is a member of WEL Project Services family of companies, along with Quimbrix, and Morvanta.
Would like BFO to mimic Quimbrix, and Morvanta in layout and functionality.
WIll use the same office address and phone # found Quimbrix and Morvanta.
The color scheme needs to match the logo colors.
The final product needs to be in word press.
would like to connect the QR code found on one-pager to the website.

Reference these websites: www.quimbrixweb.net and www.morvantaweb.net
Nice to have
• Would like to have a contact tab similar to the one found on Morvanta website. Use this email address. (BFO@WELmail.example.net)
The home page needs to have simple depictions of the problem statement, solution, and introduction to BFO. (use the video script to help, feel free to use your own words)

```html
<!DOCTYPE html>
<html lang="en">
<head>
<meta charset="utf-8">
<title>Bellcrest Field Operations</title>
<link rel="stylesheet" href="https://fonts.googleapis.com/css2?family=Roboto:wght@400;500;700&family=Russo+One&display=swap">
<style>
:root{
  --blue:#2ea3db;
  --blue-dark:#1f8cc4;
  --ink:#1d1d1d;
  --body-grey:#5a5a5a;
  --dark:#262626;
  --footer:#6c6c6e;
  --footer-bar:#5a5a5c;
  --white:#ffffff;
}
*{margin:0;padding:0;box-sizing:border-box}
html,body{width:1200px;height:2487px;overflow:hidden}
body{font-family:"Roboto",sans-serif;color:var(--ink);background:var(--white);position:relative}
.display{font-family:"Russo One",sans-serif;font-style:italic;text-transform:uppercase;letter-spacing:.5px}
section,header,footer,.footer-bar{position:absolute;left:0;width:1200px;overflow:hidden}
.abs{position:absolute}

/* header */
.site-header{top:0;height:100px;background:var(--white)}
.brand{left:112px;top:28px;display:flex;align-items:center;gap:10px;font-weight:700;font-size:40px;color:var(--blue);letter-spacing:1px}
.brand .dot{width:14px;height:14px;border-radius:50%;background:var(--blue)}
.main-nav{right:113px;top:44px;display:flex;gap:25px;font-weight:500;font-size:14.5px}
.main-nav a{color:var(--ink);text-decoration:none;position:relative}
.main-nav a.active{color:var(--blue)}
.main-nav a.active::after{content:"";position:absolute;left:3px;right:3px;bottom:-11px;height:3px;background:var(--blue)}

/* hero */
.hero{top:100px;height:601px}
.hero-photo{inset:0;background:linear-gradient(100deg,#c9d3d8 0%,#a7b6bd 40%,#8c9a7e 55%,#b8c25a 68%,#8ea9c4 82%,#c5d8ea 100%)}
.hero-veil{inset:0;background:linear-gradient(90deg,rgba(236,242,248,.94) 0%,rgba(236,242,248,.88) 45%,rgba(236,242,248,0) 62%)}
.hero-title{left:112px;top:160px;font-size:31px;line-height:43px;color:var(--blue)}
.hero-copy{left:110px;top:266px;width:530px;font-size:15.5px;line-height:27px;color:#2a2a2a}
.btn{display:inline-block;font-weight:500;text-transform:uppercase;text-decoration:none}
.btn-solid{background:var(--blue);color:var(--white)}
.hero .btn{left:110px;top:379px;width:231px;height:55px;line-height:55px;text-align:center;font-size:16.5px}
.dots{left:569px;top:540px;display:flex;gap:4px}
.dots span{width:13px;height:13px;border:2px solid #222;border-radius:50%;position:relative}
.dots span.on::after{content:"";position:absolute;inset:2px;border-radius:50%;background:#222}

/* problems */
.problems{top:701px;height:451px;background:var(--dark)}
.problems-photo{inset:0;background:linear-gradient(180deg,#3a3c3f 0%,#2a2b2d 45%,#1f2022 100%)}
.problems h2{width:100%;top:80px;text-align:center;font-size:33px;color:var(--white)}
.problem-grid{left:80px;top:167px;width:1040px;display:grid;grid-template-columns:repeat(4,1fr);text-align:center;color:var(--white)}
.problem svg{display:block;margin:0 auto 10px;width:54px;height:54px}
.problem h3{font-weight:500;font-size:17px;line-height:24px;margin-bottom:12px}
.problem p{font-size:14.5px;line-height:21.5px;padding:0 18px}

/* solution */
.solution{top:1152px;height:495px}
.solution-photo{left:0;top:0;width:620px;height:495px;background:linear-gradient(135deg,#d9e1ea 0%,#b9c6d3 40%,#e9edf1 70%,#c7b9a6 100%)}
.solution-panel{left:0;top:0;width:1200px;height:495px;background:var(--blue);clip-path:polygon(548px 0,1200px 0,1200px 495px,599px 495px)}
.solution h2{left:642px;top:64px;font-size:33px;color:var(--white)}
.solution .copy{left:643px;top:120px;width:490px;color:var(--white);font-size:14.5px;line-height:24px}
.solution .copy p+p{margin-top:12px}
.btn-light{background:var(--white);color:var(--blue)}
.solution .btn{left:643px;top:380px;width:174px;height:48px;line-height:48px;text-align:center;font-size:15px}

/* about */
.about{top:1647px;height:453px;background:var(--white)}
.about-photo{left:0;top:0;width:1200px;height:453px;background:linear-gradient(120deg,#c9d3d9 0%,#8ea2b3 35%,#d9c23a 55%,#2c63b8 75%,#b9cde0 100%);clip-path:polygon(600px 0,1200px 0,1200px 453px,661px 453px)}
.about h2{left:108px;top:62px;font-size:33px;color:var(--blue)}
.about .copy{left:111px;top:125px;width:475px;color:var(--body-grey);font-size:14.5px;line-height:24px}
.about .copy p+p{margin-top:10px}
.about .btn{left:111px;top:330px;width:174px;height:48px;line-height:48px;text-align:center;font-size:15px}

/* footer */
.site-footer{top:2100px;height:342px;background:var(--footer);color:var(--white)}
.footer-brand{left:112px;top:52px;font-weight:700;font-size:36px;display:flex;align-items:center;gap:9px;letter-spacing:1px}
.footer-brand .dot{width:12px;height:12px;border-radius:50%;background:var(--white)}
.footer-about{left:110px;top:148px;width:430px;font-size:14.5px;line-height:22.5px;text-align:justify}
.quick-links{left:635px;top:72px}
.quick-links h4{font-weight:500;font-size:17px;margin-bottom:18px}
.quick-links a{display:block;color:var(--white);text-decoration:none;font-size:14.5px;line-height:33px}
.contact-list{left:836px;top:72px;font-size:14.5px;line-height:22px}
.contact-list li{list-style:none;display:flex;gap:12px;margin-bottom:12px}
.contact-list svg{width:16px;height:16px;flex:none;margin-top:3px}
.social-square{width:20px;height:20px;border-radius:3px;background:var(--white);margin-top:4px}
.partners{left:769px;top:278px;display:flex;gap:26px;align-items:center;font-weight:700;font-size:20px}
.partners .wel{color:#1f4e9a}
.partners .quimbrix{color:#7cc242}
.partners .morvanta{color:var(--white)}
.footer-bar{top:2442px;height:45px;background:var(--footer-bar);color:var(--white);font-size:14.5px;line-height:45px;padding-left:112px}
</style>
</head>
<body>

<header class="site-header">
  <div class="abs brand"><span class="dot"></span>BFO</div>
  <nav class="abs main-nav">
    <a href="#" class="active">COMPANY</a>
    <a href="#">SOLUTIONS</a>
    <a href="#">SUPPORT</a>
    <a href="#">RESOURCES</a>
    <a href="#">COMMUNICATIONS</a>
    <a href="#">CONTACT</a>
  </nav>
</header>

<section class="hero">
  <div class="abs hero-photo" role="img" aria-label="Two engineers in blue coveralls and hard hats walking through a refinery plant"></div>
  <div class="abs hero-veil"></div>
  <h1 class="abs display hero-title">Innovative approach<br>to planning &amp; scheduling</h1>
  <p class="abs hero-copy">The impact of recent events and the ever pressing need to mitigate risk and liability in their facilities has compelled owner companies to search for economic alternatives to their typical STO event execution.</p>
  <a class="abs btn btn-solid" href="#">Scheduling Services</a>
  <div class="abs dots"><span></span><span class="on"></span><span></span><span></span></div>
</section>

<section class="problems">
  <div class="abs problems-photo" role="img" aria-label="Darkened view of a refinery skyline at night"></div>
  <h2 class="abs display">The problems</h2>
  <div class="abs problem-grid">
    <div class="problem">
      <svg viewBox="0 0 54 54" fill="none" stroke="#fff" stroke-width="2"><rect x="14" y="6" width="28" height="40" rx="2"/><line x1="20" y1="16" x2="36" y2="16"/><line x1="20" y1="24" x2="36" y2="24"/><line x1="20" y1="32" x2="36" y2="32"/><rect x="6" y="30" width="12" height="16"/></svg>
      <h3>High cost for turnaround<br>planning scheduling</h3>
      <p>Lorem ipsum sit amet, consectetur adipiscing elit, sed do eiusmod tempor quis nostrud</p>
    </div>
    <div class="problem">
      <svg viewBox="0 0 54 54" fill="none" stroke="#fff" stroke-width="2"><path d="M16 20a11 11 0 0 1 22 0z"/><line x1="13" y1="20" x2="41" y2="20"/><path d="M8 48c2-10 10-14 19-14s17 4 19 14"/><path d="M36 38l8 3v5c0 3-4 6-8 7-4-1-8-4-8-7v-5z"/></svg>
      <h3>Safety risks, social<br>distancing issues</h3>
      <p>Lorem ipsum sit amet, consectetur adipiscing elit, sed do eiusmod tempor quis nostrud</p>
    </div>
    <div class="problem">
      <svg viewBox="0 0 54 54" fill="none" stroke="#fff" stroke-width="2"><rect x="12" y="4" width="30" height="46" rx="2"/><circle cx="27" cy="15" r="5"/><line x1="18" y1="28" x2="36" y2="28"/><line x1="18" y1="34" x2="36" y2="34"/><line x1="18" y1="40" x2="30" y2="40"/></svg>
      <h3>Legal liabilities,<br>co-employment issues</h3>
      <p>Lorem ipsum sit amet, consectetur adipiscing elit, sed do eiusmod tempor quis nostrud</p>
    </div>
    <div class="problem">
      <svg viewBox="0 0 54 54" fill="none" stroke="#fff" stroke-width="2"><rect x="6" y="26" width="42" height="22"/><path d="M26 26a11 11 0 0 1 20 0"/><rect x="10" y="12" width="10" height="14"/><line x1="6" y1="38" x2="48" y2="38"/><rect x="12" y="40" width="6" height="8"/><rect x="30" y="40" width="6" height="8"/></svg>
      <h3>Distraction due to plant upsets,<br>or site interferences</h3>
      <p>Lorem ipsum sit amet, consectetur adipiscing elit, sed do eiusmod tempor quis nostrud</p>
    </div>
  </div>
</section>

<section class="solution">
  <div class="abs solution-photo" role="img" aria-label="Person at a desk reviewing charts on a computer monitor"></div>
  <div class="abs solution-panel"></div>
  <h2 class="abs display">The solution</h2>
  <div class="abs copy">
    <p>Sed ut perspiciatis unde omnis iste natus error sit voluptatem accusantium doloremque laudantium, totam rem aperiam, eaque ipsa quae ab inventore veritatis et quasi architecto beatae vitae dicta sunt explicabo. Nemo enim ipsam voluptatem quia voluptas sit aspernatur aut odit aut fugit, sed quia consequuntur magni dolores eos qui ratione voluptatem sequi nesciunt. Neque porro quisquam est, qui dolorem ipsum quia dolor sit amet, consectetur, adipisci velit, sed quia non</p>
    <p>Lorem ipsum dolor sit amet, consectetur adipiscing elit, sed do eiusmod tempor incididunt ut labore et dolore magna aliqua.</p>
  </div>
  <a class="abs btn btn-light" href="#">Give WEL a call</a>
</section>

<section class="about">
  <div class="abs about-photo" role="img" aria-label="Two engineers in hard hats inspecting equipment at a refinery"></div>
  <h2 class="abs display">About us</h2>
  <div class="abs copy">
    <p>Sed ut perspiciatis unde omnis iste natus error sit voluptatem accusantium doloremque laudantium, totam rem aperiam, eaque ipsa quae ab inventore veritatis et quasi architecto beatae vitae dicta sunt explicabo. Nemo enim ipsam voluptatem quia voluptas sit aspernatur aut odit aut fugit, sed quia consequuntur magni dolores eos qui ratione</p>
    <p>Lorem ipsum dolor sit amet, consectetur adipiscing elit, sed do eiusmod tempor incididunt ut labore et dolore magna aliqua.</p>
  </div>
  <a class="abs btn btn-solid" href="#">Ask about our BFO</a>
</section>

<footer class="site-footer">
  <div class="abs footer-brand"><span class="dot"></span>BFO</div>
  <p class="abs footer-about">The impact of recent events and the ever pressing need to mitigate risk and liability in their facilities has compelled owner companies to search for economic alternatives to their typical STO event execution.</p>
  <nav class="abs quick-links">
    <h4>Quick Links</h4>
    <a href="#">About Us</a>
    <a href="#">Solution</a>
    <a href="#">Support</a>
    <a href="#">Contact</a>
  </nav>
  <ul class="abs contact-list">
    <li><svg viewBox="0 0 16 16" fill="#fff"><path d="M8 1a5 5 0 0 0-5 5c0 4 5 9 5 9s5-5 5-9a5 5 0 0 0-5-5zm0 7a2 2 0 1 1 0-4 2 2 0 0 1 0 4z"/></svg><span>4410 Harbor Ridge Rd, Ste. 120<br>Westbay, Texas 77000</span></li>
    <li><svg viewBox="0 0 16 16" fill="#fff"><path d="M3 1l3 3-2 2c1 2 3 4 5 5l2-2 3 3-2 3C7 15 1 9 1 3z"/></svg><span>555-014-2290</span></li>
    <li><svg viewBox="0 0 16 16" fill="#fff"><path d="M1 3h14v10H1z M1 3l7 6 7-6" stroke="#6c6c6e" stroke-width="1.2"/></svg><span>BFO@WELmail.example.net</span></li>
    <li><span class="social-square" aria-label="Social profile"></span></li>
  </ul>
  <div class="abs partners">
    <span class="wel">WEL</span>
    <span class="quimbrix">Quimbrix</span>
    <span class="morvanta">Morvanta</span>
  </div>
</footer>

<div class="footer-bar">© 2021 Bellcrest Field Operations &nbsp;| All Rights Reserved &nbsp;| &nbsp;Privacy Policy</div>

</body>
</html>
```